I need a two page flyer (one page front and back) outlining our residential furniture rental options.

Title: Premium Residential Furniture Rentals

GOOD
Our Brimwell Orla Furniture Package is designed to offer a perfect balance of affordability and style, without compromising on quality. This package features a selection of functional and aesthetically pleasing furniture pieces, ideal for those looking to create a polished and professional space. With quick installation handled by our experienced in-house team, you can expect a smooth and hassle-free setup. This package ensures both convenience and value, providing a streamlined solution for your needs.
Living room, dining room and bedroom (additional bedrooms available)
- $710/month with a 3 month commitment
- $570/month with a 6 month commitment

BETTER
Our Premium Furniture Package takes comfort and style to the next level, offering an enhanced experience compared to our Orla option. Carefully selected with durability in mind, this package features high-quality, convenient furniture designed for both functionality and aesthetics. Perfect for those seeking a more refined look and superior comfort, it’s ideal for creating a sophisticated and inviting environment. With attention to detail in both design and craftsmanship, the premium package elevates any space, ensuring a higher standard of comfort and style that caters to both employees and clients.
- $1,150/month with a 3 month commitment
- $900/month with a 6 month commitment

BEST
Our Custom Furniture Package offers a tailored experience where you’ll work directly with our expert designer to create the ultimate luxurious and functional space. We include lounging, dining, sleeping and working from home, this package allows you to curate a space that perfectly fits your needs and style. With personalized attention to detail, we ensure every element is designed to provide the highest level of comfort, convenience, and elegance, transforming your space into a sophisticated sanctuary for relaxation and enjoyment.
Please inquire for pricing

www.quilbyhomeleasing.com

```html
<!DOCTYPE html>
<html lang="en">
<head>
<meta charset="utf-8">
<title>Quilby Home Leasing — Premium Residential Furniture Rentals</title>
<link href="https://fonts.googleapis.com/css2?family=Montserrat:ital,wght@0,300;0,400;0,500;0,600;0,700;0,800;0,900;1,800&display=swap" rel="stylesheet">
<style>
  :root {
    --navy: #1f2a5e;
    --gold: #d6b928;
    --backdrop: #6b6b6d;
    --paper: #ffffff;
    --body-text: #6e6e74;
    --ink: #232323;
  }
  * { box-sizing: border-box; margin: 0; padding: 0; }
  html, body { width: 1200px; height: 2968px; overflow: hidden; }
  body { background: var(--backdrop); font-family: "Montserrat", sans-serif; position: relative; }

  .page { position: absolute; left: 100px; width: 1000px; height: 1414px; background: var(--paper); overflow: hidden; }
  .page--front { top: 47px; }
  .page--back { top: 1507px; }

  /* Front */
  .photo { position: absolute; }
  .photo--living { left: 0; top: 0; width: 489px; height: 686px; background: linear-gradient(170deg, #f2f1ee 0%, #e3e0db 55%, #b28a63 80%, #8d6a4c 100%); }
  .photo--kitchen { left: 517px; top: 0; width: 483px; height: 686px; background: linear-gradient(175deg, #f4f4f2 0%, #e6e6e3 60%, #c9a27a 85%, #a67d56 100%); }
  .photo--bedroom { left: 0; top: 710px; width: 489px; height: 704px; background: linear-gradient(170deg, #f1efec 0%, #d8d3cc 40%, #b98d66 70%, #8b6549 100%); }
  .photo--lounge { left: 517px; top: 710px; width: 483px; height: 704px; background: linear-gradient(175deg, #f3f3f3 0%, #e4e4e4 55%, #bdbdbd 85%, #9a9a9a 100%); }
  .frame-lines { position: absolute; inset: 0; }

  .brand-card { position: absolute; left: 262px; top: 469px; width: 480px; height: 340px; background: var(--paper); text-align: center; }
  .brand-mark { width: 40px; height: 40px; border: 4px solid var(--navy); margin: 70px auto 0; }
  .brand-name { margin-top: 34px; font-size: 31px; font-weight: 400; color: var(--ink); letter-spacing: 1px; }
  .brand-sub { display: flex; align-items: center; justify-content: center; gap: 18px; margin-top: 12px; font-size: 18px; letter-spacing: 14px; color: var(--ink); }
  .brand-sub::before, .brand-sub::after { content: ""; width: 52px; height: 2px; background: var(--ink); }
  .brand-services { margin-top: 16px; font-size: 13px; font-weight: 500; color: var(--navy); letter-spacing: 1.5px; }

  .title-band { position: absolute; left: 262px; top: 809px; width: 480px; height: 139px; background: var(--navy); color: #fff; display: flex; align-items: center; justify-content: center; text-align: center; font-weight: 800; font-size: 33px; line-height: 1.22; letter-spacing: .5px; }

  /* Back */
  .tier { position: absolute; left: 76px; width: 850px; border: 4px solid var(--navy); }
  .tier::after { content: ""; position: absolute; right: -6px; width: 8px; height: 30px; background: var(--paper); bottom: 36px; }
  .tier--good { top: 60px; height: 365px; }
  .tier--better { top: 469px; height: 364px; }
  .tier--best { top: 877px; height: 320px; }
  .tier-name { position: absolute; left: 43px; top: 14px; font-size: 50px; font-weight: 900; color: var(--navy); letter-spacing: 1px; }
  .tier-copy { position: absolute; left: 43px; top: 92px; width: 432px; font-size: 13px; line-height: 19px; font-weight: 400; color: var(--body-text); text-align: justify; }
  .tier--best .tier-copy { width: 766px; }
  .tier-rooms { position: absolute; left: 43px; bottom: 30px; font-size: 13px; font-weight: 600; color: var(--ink); line-height: 16px; }
  .tier-rooms small { display: block; font-size: 11px; font-weight: 400; color: var(--body-text); }

  .price { position: absolute; left: 518px; width: 270px; height: 112px; padding: 18px 0 0 24px; }
  .price--navy { background: var(--navy); top: 53px; }
  .price--gold { background: var(--gold); top: 190px; }
  .price-figure { display: flex; align-items: center; gap: 6px; }
  .price-amount { font-size: 52px; font-weight: 900; letter-spacing: -1px; line-height: 1; }
  .price--navy .price-amount { color: var(--gold); }
  .price--gold .price-amount { color: var(--navy); }
  .price-unit { background: #fff; color: var(--navy); font-size: 19px; font-weight: 800; font-style: italic; padding: 1px 12px 1px 8px; clip-path: polygon(6% 0, 100% 0, 100% 100%, 0 100%); }
  .price-term { margin-top: 8px; font-size: 13px; font-weight: 400; }
  .price--navy .price-term { color: #b9bdd0; }
  .price--gold .price-term { color: #fff; }
  .price-term b { font-weight: 700; }
  .price--navy .price-term b { color: #fff; }
  .price--gold .price-term b { color: var(--navy); }

  .inquire-bar { position: absolute; left: 43px; top: 208px; width: 766px; height: 60px; display: flex; }
  .inquire-label { width: 328px; background: var(--gold); color: var(--navy); font-size: 17px; font-weight: 600; display: flex; align-items: center; padding-left: 34px; }
  .inquire-site { flex: 1; background: var(--navy); color: #fff; font-size: 21px; display: flex; align-items: center; gap: 14px; padding-left: 6px; }
  .inquire-site b { font-weight: 700; }
  .globe { width: 34px; height: 34px; border-radius: 50%; background: #fff; display: flex; align-items: center; justify-content: center; }

  .contact-band { position: absolute; left: 0; top: 1241px; width: 1000px; height: 173px; background: var(--gold); text-align: center; color: #fff; padding-top: 22px; }
  .contact-title { font-size: 28px; font-weight: 500; letter-spacing: .5px; }
  .contact-address { margin-top: 8px; font-size: 20px; font-weight: 400; display: flex; justify-content: center; align-items: center; gap: 6px; }
  .contact-phone { margin-top: 10px; font-size: 48px; font-weight: 800; color: var(--navy); display: flex; justify-content: center; align-items: center; gap: 10px; letter-spacing: 1px; }
</style>
</head>
<body>

<section class="page page--front">
  <div class="photo photo--living" role="img" aria-label="Furnished living room with armchairs, rug and wall art"></div>
  <div class="photo photo--kitchen" role="img" aria-label="Bright white kitchen with dining table and chairs"></div>
  <div class="photo photo--bedroom" role="img" aria-label="Bedroom with upholstered bed and patterned armchairs"></div>
  <div class="photo photo--lounge" role="img" aria-label="Lounge with white brick fireplace and sofa"></div>

  <svg class="frame-lines" width="1000" height="1414" viewBox="0 0 1000 1414" aria-hidden="true">
    <g stroke="#1f2a5e" stroke-width="4" fill="none">
      <line x1="24" y1="42" x2="978" y2="42"/>
      <line x1="26" y1="40" x2="26" y2="778"/>
      <line x1="26" y1="878" x2="26" y2="1376"/>
      <line x1="24" y1="1374" x2="978" y2="1374"/>
      <line x1="976" y1="40" x2="976" y2="1019"/>
      <line x1="976" y1="1160" x2="976" y2="1376"/>
    </g>
  </svg>

  <div class="brand-card">
    <div class="brand-mark"></div>
    <div class="brand-name">QUILBY HOME</div>
    <div class="brand-sub">LEASING</div>
    <div class="brand-services">STAGING | RESIDENTIAL | CORPORATE | SALES</div>
  </div>
  <div class="title-band">PREMIUM RESIDENTIAL<br>FURNITURE RENTALS</div>
</section>

<section class="page page--back">
  <article class="tier tier--good">
    <h2 class="tier-name">GOOD</h2>
    <p class="tier-copy">Our Brimwell Orla Furniture Package is designed to offer a perfect balance of affordability and style, without compromising on quality. This package features a selection of functional and aesthetically pleasing furniture pieces, ideal for those looking to create a polished and professional space. With quick installation handled by our experienced in-house team, you can expect a smooth and hassle-free setup. This package ensures both convenience and value, providing a streamlined solution for your needs.</p>
    <p class="tier-rooms">Living room, dining room and bedroom<small>(additional bedrooms available)</small></p>
    <div class="price price--navy">
      <div class="price-figure"><span class="price-amount">$710</span><span class="price-unit">/month</span></div>
      <div class="price-term">with a <b>3 month</b> commitment</div>
    </div>
    <div class="price price--gold">
      <div class="price-figure"><span class="price-amount">$570</span><span class="price-unit">/month</span></div>
      <div class="price-term">with a <b>6 month</b> commitment</div>
    </div>
  </article>

  <article class="tier tier--better">
    <h2 class="tier-name">BETTER</h2>
    <p class="tier-copy">Our Premium Furniture Package takes comfort and style to the next level, offering an enhanced experience compared to our Orla option. Carefully selected with durability in mind, this package features high-quality, convenient furniture designed for both functionality and aesthetics. Perfect for those seeking a more refined look and superior comfort, it’s ideal for creating a sophisticated and inviting environment. With attention to detail in both design and craftsmanship, the premium package elevates any space, ensuring a higher standard of comfort and style that caters to both employees and clients.</p>
    <p class="tier-rooms">Living room, dining room and bedroom<small>(additional bedrooms available)</small></p>
    <div class="price price--navy">
      <div class="price-figure"><span class="price-amount">$1,150</span><span class="price-unit">/month</span></div>
      <div class="price-term">with a <b>3 month</b> commitment</div>
    </div>
    <div class="price price--gold">
      <div class="price-figure"><span class="price-amount">$900</span><span class="price-unit">/month</span></div>
      <div class="price-term">with a <b>6 month</b> commitment</div>
    </div>
  </article>

  <article class="tier tier--best">
    <h2 class="tier-name">BEST</h2>
    <p class="tier-copy">Our Custom Furniture Package offers a tailored experience where you’ll work directly with our expert designer to create the ultimate luxurious and functional space. We include lounging, dining, sleeping and working from home, this package allows you to curate a space that perfectly fits your needs and style. With personalized attention to detail, we ensure every element is designed to provide the highest level of comfort, convenience, and elegance, transforming your space into a sophisticated sanctuary for relaxation and enjoyment.</p>
    <div class="inquire-bar">
      <div class="inquire-label">PLEASE INQUIRE FOR PRICING</div>
      <div class="inquire-site">
        <span class="globe">
          <svg width="26" height="26" viewBox="0 0 26 26" aria-hidden="true"><g fill="none" stroke="#1f2a5e" stroke-width="1.8"><circle cx="13" cy="13" r="11"/><ellipse cx="13" cy="13" rx="5" ry="11"/><line x1="2" y1="13" x2="24" y2="13"/><line x1="4" y1="7.5" x2="22" y2="7.5"/><line x1="4" y1="18.5" x2="22" y2="18.5"/></g></svg>
        </span>
        <span>www.<b>quilbyhomeleasing</b>.com</span>
      </div>
    </div>
  </article>

  <footer class="contact-band">
    <div class="contact-title">RESIDENTIAL FURNITURE RENTAL</div>
    <div class="contact-address">
      <svg width="14" height="18" viewBox="0 0 14 18" aria-hidden="true"><path d="M7 0C3.1 0 0 3.1 0 7c0 5 7 11 7 11s7-6 7-11c0-3.9-3.1-7-7-7zm0 9.5A2.5 2.5 0 1 1 7 4.5a2.5 2.5 0 0 1 0 5z" fill="#fff"/></svg>
      4120 Marlow Bend Suite 310, Fairhaven, Texas 77099, United States
    </div>
    <div class="contact-phone">
      <svg width="34" height="34" viewBox="0 0 24 24" aria-hidden="true"><path d="M6.6 10.8a15.1 15.1 0 0 0 6.6 6.6l2.2-2.2c.3-.3.7-.4 1-.2 1.1.4 2.3.6 3.6.6.6 0 1 .4 1 1V20c0 .6-.4 1-1 1A17 17 0 0 1 3 4c0-.6.4-1 1-1h3.5c.6 0 1 .4 1 1 0 1.3.2 2.5.6 3.6.1.3 0 .7-.2 1z" fill="#fff"/></svg>
      555-240-7719
    </div>
  </footer>
</section>

</body>
</html>
```